Scheduled Servicing Forms

Lumenridge Systems requires two schedule servicing forms to be created on designer templates for our engineers to complete when servicing customers. We will complete these forms on a periodic basis, and send to the customer on completion of the work.
We have two forms that need to be created:
• Hybrid Cloud Customer Service
• Norvex Cloud Customer Service
Please do not reference our website for ideas as its about to change. “Specialised Consulting” is our new go to market, not “Charting the Frontiers of Computing. Our new website (still under development) is available at https://lumenridgesystems.qxv.net.au and will be officially launched shortly.
Our company theme is “Blue” and we want to keep a blue theme for the work.
Please ensure there is “Ample” space for engineers to write comments next to each audit item.
We have uploaded examples of the content that needs to be created for both form in Word and Excel format.
The designer must upload the source files (not just PDF) so we can edit the content on the forms at a later date.
The forms must be in standard A4 size (multiple pages).

```html
<!DOCTYPE html>
<html lang="en">
<head>
<meta charset="utf-8">
<title>Scheduled Service Checklist – Norvex Hybrid/On-Premise</title>
<link rel="stylesheet" href="https://fonts.googleapis.com/css2?family=Open+Sans:wght@400;600;700&display=swap">
<style>
:root{
  --stage:#b3b3b3;
  --navy:#14207a;
  --blue-deep:#0a1fa8;
  --blue-mid:#1c4fe0;
  --blue-light:#2f7cf2;
  --panel:#eaf6fb;
  --rule:#8d98c8;
  --white:#ffffff;
  --tab-a:#b4b9c2;
  --tab-b:#5d636d;
}
*{box-sizing:border-box;margin:0;padding:0}
html,body{width:1200px;height:848px;overflow:hidden;background:var(--stage);font-family:"Open Sans",Arial,sans-serif;color:var(--navy)}
.canvas{position:relative;width:1200px;height:848px}
.page{position:absolute;width:280px;height:397px;overflow:hidden;
  background:radial-gradient(ellipse at 70% 35%,var(--blue-light) 0%,var(--blue-mid) 40%,var(--blue-deep) 100%)}
.page-head{position:absolute;left:0;top:0;width:100%;height:28px;background:var(--white);
  display:flex;align-items:center;justify-content:space-between;padding:0 22px 0 10px}
.page-head::after{content:"";position:absolute;right:0;top:0;width:20px;height:28px;
  background:linear-gradient(135deg,transparent 48%,#c9ccd3 49%,#8e939c 66%,transparent 67%)}
.brand{display:flex;align-items:center;gap:4px;font-size:7px;font-weight:700;color:var(--navy);letter-spacing:.2px}
.brand-mark{width:9px;height:9px;background:var(--blue-mid)}
.form-title{font-size:7.6px;font-weight:700;color:var(--navy);white-space:nowrap}
.info{position:absolute;left:9px;top:44px;width:140px;height:43px;background:var(--panel);padding:3px 4px;font-size:5px}
.info h2{font-size:7px;font-weight:700;margin-bottom:2px}
.field{display:flex;align-items:flex-end;gap:2px;margin-top:4px}
.field span{flex:1;border-bottom:.6px solid var(--navy);height:5px}
.page-no{position:absolute;left:194px;top:54px;width:42px;height:17px;border:1px solid var(--white);
  color:var(--white);font-size:8px;font-weight:600;display:flex;align-items:center;justify-content:center}
.frame{position:absolute;left:6px;top:98px;width:268px;height:292px;border:1px solid rgba(200,210,240,.7);
  box-shadow:inset 0 0 0 2px rgba(10,20,110,.5),inset 0 0 0 3px rgba(200,210,240,.5)}
.tab{position:absolute;z-index:2;top:92px;height:13px;width:56px;font-size:4px;color:var(--white);
  display:flex;align-items:center;justify-content:center;text-transform:uppercase;white-space:nowrap;
  background:linear-gradient(180deg,var(--tab-a),var(--tab-b));clip-path:polygon(0 0,100% 0,90% 100%,10% 100%)}
.tab-check{left:38px}
.tab-result{left:187px}
.checks{position:absolute;left:12px;top:112px;width:256px;display:flex;flex-direction:column;gap:7.6px}
.check{height:47px;background:var(--panel);display:grid;grid-template-columns:134px 1fr}
.check.tall{height:101.6px}
.item{display:flex;flex-direction:column;align-items:center;justify-content:center;text-align:center;
  font-size:5px;line-height:1.3;padding:0 6px}
.item small{font-size:3.6px;line-height:1.2}
.result{padding:3px 6px 0 0;font-size:4.3px}
.yn{display:flex;gap:5px;font-size:5px;margin-bottom:1px}
.yn i{display:inline-block;width:5px;height:5px;border:.6px solid var(--navy);margin-right:1.5px;vertical-align:-1px}
.line{display:flex;gap:2px;height:6.2px;align-items:flex-end}
.line span{flex:1;border-bottom:.5px solid var(--rule)}
.line.short span{flex:0 0 30px}
</style>
</head>
<body>
<div class="canvas">

<!-- Page 1 -->
<section class="page" style="left:135px;top:19px">
  <header class="page-head"><div class="brand"><span class="brand-mark"></span>Lumenridge Systems</div><div class="form-title">Norvex Hybrid/On-Premise</div></header>
  <div class="info"><h2>Scheduled Service Checklist</h2><div class="field">Date:<span></span></div><div class="field">Customer:<span></span></div></div>
  <div class="page-no">Page 1</div>
  <div class="frame"></div>
  <div class="tab tab-check">Maintainance check</div><div class="tab tab-result">Result</div>
  <div class="checks">
    <div class="check"><div class="item">Active backup for all Suite accounts<small>(manual check)</small>Ensuring all items are included in the job</div><div class="result"><div class="yn"><span><i></i>YES</span><span><i></i>NO</span></div><div class="line">Comment:<span></span></div><div class="line"><span></span></div><div class="line"><span></span></div><div class="line"><span></span></div></div></div>
    <div class="check"><div class="item">Test restore from server backup</div><div class="result"><div class="yn"><span><i></i>YES</span><span><i></i>NO</span></div><div class="line">Comment:<span></span></div><div class="line"><span></span></div><div class="line"><span></span></div><div class="line"><span></span></div></div></div>
    <div class="check"><div class="item">Test restore of an email</div><div class="result"><div class="yn"><span><i></i>YES</span><span><i></i>NO</span></div><div class="line">Comment:<span></span></div><div class="line"><span></span></div><div class="line"><span></span></div><div class="line"><span></span></div></div></div>
    <div class="check"><div class="item">Test restore of DocuHarbor file</div><div class="result"><div class="yn"><span><i></i>YES</span><span><i></i>NO</span></div><div class="line">Comment:<span></span></div><div class="line"><span></span></div><div class="line"><span></span></div><div class="line"><span></span></div></div></div>
    <div class="check"><div class="item">Log into Antivirus products<small>(ensure all endpoint devices have<br>active antivirus and are up to date)</small></div><div class="result"><div class="yn"><span><i></i>YES</span><span><i></i>NO</span></div><div class="line">Comment:<span></span></div><div class="line"><span></span></div><div class="line"><span></span></div><div class="line"><span></span></div></div></div>
  </div>
</section>

<!-- Page 2 -->
<section class="page" style="left:447px;top:19px">
  <header class="page-head"><div class="brand"><span class="brand-mark"></span>Lumenridge Systems</div><div class="form-title">Norvex Hybrid/On-Premise</div></header>
  <div class="info"><h2>Scheduled Service Checklist</h2><div class="field">Date:<span></span></div><div class="field">Customer:<span></span></div></div>
  <div class="page-no">Page 2</div>
  <div class="frame"></div>
  <div class="tab tab-check">Maintainance check</div><div class="tab tab-result">Result</div>
  <div class="checks">
    <div class="check"><div class="item">Check Spam filters</div><div class="result"><div class="yn"><span><i></i>YES</span><span><i></i>NO</span></div><div class="line">Comment:<span></span></div><div class="line"><span></span></div><div class="line"><span></span></div><div class="line"><span></span></div></div></div>
    <div class="check"><div class="item">Check that all users have MFA enabled</div><div class="result"><div class="yn"><span><i></i>YES</span><span><i></i>NO</span></div><div class="line">Comment:<span></span></div><div class="line"><span></span></div><div class="line"><span></span></div><div class="line"><span></span></div></div></div>
    <div class="check"><div class="item">Review Norvex Suite Risk Detections</div><div class="result"><div class="yn"><span><i></i>YES</span><span><i></i>NO</span></div><div class="line">Comment:<span></span></div><div class="line"><span></span></div><div class="line"><span></span></div><div class="line"><span></span></div></div></div>
    <div class="check"><div class="item">Confirm Audit Log enabled</div><div class="result"><div class="yn"><span><i></i>YES</span><span><i></i>NO</span></div><div class="line">Comment:<span></span></div><div class="line"><span></span></div><div class="line"><span></span></div><div class="line"><span></span></div></div></div>
    <div class="check"><div class="item">Review Norvex Suite license expiry dates</div><div class="result"><div class="line short">Expiry Date:<span></span></div><div class="line">Comment:<span></span></div><div class="line"><span></span></div><div class="line"><span></span></div><div class="line"><span></span></div></div></div>
  </div>
</section>

<!-- Page 3 -->
<section class="page" style="left:761px;top:19px">
  <header class="page-head"><div class="brand"><span class="brand-mark"></span>Lumenridge Systems</div><div class="form-title">Norvex Hybrid/On-Premise</div></header>
  <div class="info"><h2>Scheduled Service Checklist</h2><div class="field">Date:<span></span></div><div class="field">Customer:<span></span></div></div>
  <div class="page-no">Page 3</div>
  <div class="frame"></div>
  <div class="tab tab-check">Maintainance check</div><div class="tab tab-result">Result</div>
  <div class="checks">
    <div class="check"><div class="item">Review external sharing in<br>DocuHarbor/FileNest</div><div class="result"><div class="yn"><span><i></i>YES</span><span><i></i>NO</span></div><div class="line">Comment:<span></span></div><div class="line"><span></span></div><div class="line"><span></span></div><div class="line"><span></span></div></div></div>
    <div class="check"><div class="item">Check Compliance status</div><div class="result"><div class="yn"><span><i></i>YES</span><span><i></i>NO</span></div><div class="line">Comment:<span></span></div><div class="line"><span></span></div><div class="line"><span></span></div><div class="line"><span></span></div></div></div>
    <div class="check tall"><div class="item">Check and record Norvex security score</div><div class="result"><div class="yn"><span><i></i>YES</span><span><i></i>NO</span></div><div class="line short">Score:<span></span></div><div class="line">Top 5 Recommendations:</div><div class="line">1.<span></span></div><div class="line">2.<span></span></div><div class="line">3.<span></span></div><div class="line">4.<span></span></div><div class="line">5.<span></span></div><div class="line">Comment:<span></span></div><div class="line"><span></span></div><div class="line"><span></span></div></div></div>
    <div class="check"><div class="item">Conditional access Rules<small>(no silly Rules, Geolocation filters in place for<br>Sanctioned Countries)</small></div><div class="result"><div class="yn"><span><i></i>YES</span><span><i></i>NO</span></div><div class="line">Comment:<span></span></div><div class="line"><span></span></div><div class="line"><span></span></div><div class="line"><span></span></div></div></div>
  </div>
</section>

<!-- Page 4 -->
<section class="page" style="left:135px;top:440px">
  <header class="page-head"><div class="brand"><span class="brand-mark"></span>Lumenridge Systems</div><div class="form-title">Norvex Hybrid/On-Premise</div></header>
  <div class="info"><h2>Scheduled Service Checklist</h2><div class="field">Date:<span></span></div><div class="field">Customer:<span></span></div></div>
  <div class="page-no">Page 4</div>
  <div class="frame"></div>
  <div class="tab tab-check">Maintainance check</div><div class="tab tab-result">Result</div>
  <div class="checks">
    <div class="check"><div class="item">Review security access of all<br>privileged access accounts</div><div class="result"><div class="yn"><span><i></i>YES</span><span><i></i>NO</span></div><div class="line">Comment:<span></span></div><div class="line"><span></span></div><div class="line"><span></span></div><div class="line"><span></span></div></div></div>
    <div class="check"><div class="item">Review Application Patching<br>and confirm all workstations<br>&amp; servers are up to date</div><div class="result"><div class="yn"><span><i></i>YES</span><span><i></i>NO</span></div><div class="line">Comment:<span></span></div><div class="line"><span></span></div><div class="line"><span></span></div><div class="line"><span></span></div></div></div>
    <div class="check"><div class="item">Review Desktop OS Patching<br>and confirm all workstations<br>&amp; servers are up to date</div><div class="result"><div class="yn"><span><i></i>YES</span><span><i></i>NO</span></div><div class="line">Comment:<span></span></div><div class="line"><span></span></div><div class="line"><span></span></div><div class="line"><span></span></div></div></div>
    <div class="check"><div class="item">Review domain expiry dates</div><div class="result"><div class="line short">Expiry Date:<span></span></div><div class="line">Comment:<span></span></div><div class="line"><span></span></div><div class="line"><span></span></div><div class="line"><span></span></div></div></div>
    <div class="check"><div class="item">Review certificate expiry dates<small>(including internal services i.e. vHost Manager)</small></div><div class="result"><div class="line short">Expiry Date:<span></span></div><div class="line">Comment:<span></span></div><div class="line"><span></span></div><div class="line"><span></span></div><div class="line"><span></span></div></div></div>
  </div>
</section>

<!-- Page 5 -->
<section class="page" style="left:447px;top:440px">
  <header class="page-head"><div class="brand"><span class="brand-mark"></span>Lumenridge Systems</div><div class="form-title">Norvex Hybrid/On-Premise</div></header>
  <div class="info"><h2>Scheduled Service Checklist</h2><div class="field">Date:<span></span></div><div class="field">Customer:<span></span></div></div>
  <div class="page-no">Page 5</div>
  <div class="frame"></div>
  <div class="tab tab-check">Maintainance check</div><div class="tab tab-result">Result</div>
  <div class="checks">
    <div class="check"><div class="item">Confirm all devices are in Application<br>Whitelisting enforcement mode</div><div class="result"><div class="yn"><span><i></i>YES</span><span><i></i>NO</span></div><div class="line">Comment:<span></span></div><div class="line"><span></span></div><div class="line"><span></span></div><div class="line"><span></span></div></div></div>
    <div class="check"><div class="item">Ensure DMARC, DKIM and SPF<br>records are in place and up to date</div><div class="result"><div class="yn"><span><i></i>YES</span><span><i></i>NO</span></div><div class="line">Comment:<span></span></div><div class="line"><span></span></div><div class="line"><span></span></div><div class="line"><span></span></div></div></div>
    <div class="check"><div class="item">Confirm Retention Policies is<br>configured and time specified</div><div class="result"><div class="yn"><span><i></i>YES</span><span><i></i>NO</span></div><div class="line">Comment:<span></span></div><div class="line"><span></span></div><div class="line"><span></span></div><div class="line"><span></span></div></div></div>
    <div class="check"><div class="item">Review Network Firewall Firmware<br>is up to date and no<br>ANY &lt;&gt; ANY rules in place</div><div class="result"><div class="yn"><span><i></i>YES</span><span><i></i>NO</span></div><div class="line">Comment:<span></span></div><div class="line"><span></span></div><div class="line"><span></span></div><div class="line"><span></span></div></div></div>
    <div class="check"><div class="item">Ensure critical network equipment<br>is connected to UPS<small>(min 20min run time)</small></div><div class="result"><div class="yn"><span><i></i>YES</span><span><i></i>NO</span></div><div class="line">Comment:<span></span></div><div class="line"><span></span></div><div class="line"><span></span></div><div class="line"><span></span></div></div></div>
  </div>
</section>

<!-- Page 6 -->
<section class="page" style="left:761px;top:440px">
  <header class="page-head"><div class="brand"><span class="brand-mark"></span>Lumenridge Systems</div><div class="form-title">Norvex Hybrid/On-Premise</div></header>
  <div class="info"><h2>Scheduled Service Checklist</h2><div class="field">Date:<span></span></div><div class="field">Customer:<span></span></div></div>
  <div class="page-no">Page 6</div>
  <div class="frame"></div>
  <div class="tab tab-check">Maintainance check</div><div class="tab tab-result">Result</div>
  <div class="checks">
    <div class="check"><div class="item">Ensure Access Layer Network device<br>firmware is up to date<small>(Switches &amp; Access Points)</small></div><div class="result"><div class="yn"><span><i></i>YES</span><span><i></i>NO</span></div><div class="line">Comment:<span></span></div><div class="line"><span></span></div><div class="line"><span></span></div><div class="line"><span></span></div></div></div>
    <div class="check"><div class="item">Ensure the latest backup configuration for<br>managed network devices is current or<br>automatically backed up monthly.<br>Saved Network location must be secured</div><div class="result"><div class="yn"><span><i></i>YES</span><span><i></i>NO</span></div><div class="line">Comment:<span></span></div><div class="line"><span></span></div><div class="line"><span></span></div><div class="line"><span></span></div></div></div>
    <div class="check"><div class="item">Ensure MFP's &amp; Printers drivers up to date.<br>No Print Nightmare</div><div class="result"><div class="yn"><span><i></i>YES</span><span><i></i>NO</span></div><div class="line">Comment:<span></span></div><div class="line"><span></span></div><div class="line"><span></span></div><div class="line"><span></span></div></div></div>
    <div class="check"><div class="item">NAC Certificates are current<small>(PEAP/EAP-TLS)</small></div><div class="result"><div class="yn"><span><i></i>YES</span><span><i></i>NO</span></div><div class="line">Comment:<span></span></div><div class="line"><span></span></div><div class="line"><span></span></div><div class="line"><span></span></div></div></div>
    <div class="check"><div class="item">Check DLP alerts and configuration</div><div class="result"><div class="yn"><span><i></i>YES</span><span><i></i>NO</span></div><div class="line">Comment:<span></span></div><div class="line"><span></span></div><div class="line"><span></span></div><div class="line"><span></span></div></div></div>
  </div>
</section>

</div>
</body>
</html>
```